Small Accounting Practice needs something creative

We need a business card design for a new small accounting practice based in Perth, Australia. The name of the practice is 'Kowra Ledger Partners Pty Ltd'. We providing Tax, Bookkeeping and Accounting services. Our target are individuals and small businesses. We want the design to be simply and creative. Also, we can the design can help us to gain people's trust.

Target Market(s)

Individuals and small businesses.

Industry/Entity Type

Accounting

Colors

Designer to choose colors to be used in the design.

```html
<!DOCTYPE html>
<html lang="en">
<head>
<meta charset="utf-8">
<title>Kowra Ledger Partners – Business Card</title>
<link rel="stylesheet" href="https://fonts.googleapis.com/css2?family=Open+Sans:wght@400;600;700&display=swap">
<style>
  :root {
    --backdrop: #e9ebee;
    --card: #ffffff;
    --ink: #2b2b2b;
    --ink-soft: #4a4a4a;
    --brand-blue: #2b8ae6;
    --icon-blue: #2e93ea;
  }
  * { box-sizing: border-box; margin: 0; padding: 0; }
  html, body {
    width: 1200px; height: 897px; overflow: hidden;
    background: var(--backdrop);
    font-family: "Open Sans", Arial, sans-serif;
    color: var(--ink);
  }
  .stage {
    width: 1200px; height: 897px;
    display: flex; align-items: center; justify-content: center; gap: 44px;
  }
  .card {
    width: 520px; height: 300px;
    background: var(--card);
    border-radius: 30px;
    box-shadow: 0 10px 30px rgba(0,0,0,0.12);
    position: relative;
  }

  /* Contact side */
  .card-back .person {
    position: absolute; left: 44px; bottom: 54px;
  }
  .person-name {
    font-size: 19px; font-weight: 700; letter-spacing: 0.5px; text-transform: uppercase;
  }
  .person-name .surname { font-weight: 400; }
  .person-title {
    font-size: 10.5px; letter-spacing: 0.4px; text-transform: uppercase; color: var(--ink-soft);
    margin-top: 2px;
  }
  .contacts {
    position: absolute; right: 36px; top: 44px;
    display: grid; grid-template-columns: auto auto; column-gap: 26px; row-gap: 22px;
  }
  .contact-row { display: flex; align-items: center; gap: 9px; }
  .contact-icon {
    width: 26px; height: 26px; flex: none;
    background: var(--icon-blue); border-radius: 5px;
    display: flex; align-items: center; justify-content: center;
  }
  .contact-icon svg { width: 15px; height: 15px; }
  .contact-text {
    font-size: 10px; line-height: 1.35; letter-spacing: 0.3px; text-transform: uppercase; color: var(--ink-soft);
  }

  /* Brand side */
  .card-front {
    display: flex; align-items: center; justify-content: center; gap: 14px;
  }
  .brand-dot {
    width: 22px; height: 22px; border-radius: 50%; background: var(--brand-blue); flex: none;
  }
  .brand-name {
    font-size: 27px; font-weight: 600; color: var(--brand-blue); line-height: 1.15;
  }
</style>
</head>
<body>
<main class="stage">
  <section class="card card-back" aria-label="Contact side">
    <div class="contacts">
      <div class="contact-row">
        <span class="contact-icon"><svg viewBox="0 0 24 24" fill="#fff"><path d="M6.6 10.8a15.1 15.1 0 0 0 6.6 6.6l2.2-2.2a1 1 0 0 1 1-.25 11.4 11.4 0 0 0 3.6.57 1 1 0 0 1 1 1V20a1 1 0 0 1-1 1A17 17 0 0 1 3 4a1 1 0 0 1 1-1h3.5a1 1 0 0 1 1 1c0 1.25.2 2.45.57 3.57a1 1 0 0 1-.25 1z"/></svg></span>
        <p class="contact-text">08 9421 5530<br>08 9421 5531</p>
      </div>
      <div class="contact-row">
        <span class="contact-icon"><svg viewBox="0 0 24 24" fill="none" stroke="#fff" stroke-width="1.8"><circle cx="12" cy="12" r="9"/><ellipse cx="12" cy="12" rx="4" ry="9"/><path d="M3 12h18M5 7h14M5 17h14"/></svg></span>
        <p class="contact-text">www.kowraledger.com.au<br>kowraledger.com.au</p>
      </div>
      <div class="contact-row">
        <span class="contact-icon"><svg viewBox="0 0 24 24" fill="none" stroke="#fff" stroke-width="1.8"><rect x="3" y="5" width="18" height="14" rx="1.5"/><path d="M3 6l9 7 9-7"/></svg></span>
        <p class="contact-text">hello@kowraledger.com.au<br>info@kowraledger.com.au</p>
      </div>
      <div class="contact-row">
        <span class="contact-icon"><svg viewBox="0 0 24 24" fill="#fff"><path d="M12 2a7 7 0 0 0-7 7c0 5.2 7 13 7 13s7-7.8 7-13a7 7 0 0 0-7-7zm0 9.5A2.5 2.5 0 1 1 12 6.5a2.5 2.5 0 0 1 0 5z"/></svg></span>
        <p class="contact-text">42 Hay Street, Perth WA 6000<br>Australia</p>
      </div>
    </div>
    <div class="person">
      <h1 class="person-name">Liam <span class="surname">Corrigan</span></h1>
      <p class="person-title">Senior Graphic Designer</p>
    </div>
  </section>

  <section class="card card-front" aria-label="Brand side">
    <span class="brand-dot"></span>
    <h2 class="brand-name">Kowra Ledger<br>Partners</h2>
  </section>
</main>
</body>
</html>
```